Astrology Reading Website to attract clients

I need a website for my astrology practice. My business name is Velvet Harbor Astrology. I will need a page the following pages: About, Readings, Booking, Contact, and Blog. I will need full figma or figma-like mockups of pages along with assets. I will need both desktop and mobile designs.
I like creams, dark blues and greens. I am fine with planets or other astrology symbolism.

Target Market(s)

new age, spiritual

Industry/Entity Type

Holistic, spiritual

Number of Pages Required

3 page

Colors
0054AA
0677BA
7BADD7
CADEEF
E8F1F8

Requirements
Nice to have
• calm and grounded backgrounds

```html
<!DOCTYPE html>
<html lang="en">
<head>
<meta charset="utf-8">
<title>Velvet Harbor Astrology — About and Readings</title>
<link rel="stylesheet" href="https://fonts.googleapis.com/css2?family=Gideon+Roman&family=Poppins:wght@300;400;500;600&display=swap">
<style>
  :root {
    --stage: #2c2c2e;
    --nav: #212535;
    --night: #1b2031;
    --night-mid: #2a3047;
    --card: rgba(52, 58, 80, 0.55);
    --card-line: rgba(190, 200, 230, 0.22);
    --footer: #272839;
    --field: #45465a;
    --field-text: #b9bac6;
    --cream: #fdf3e1;
    --text: #e9e6df;
    --muted: #c8c6c4;
    --green: #a6ff5c;
    --ink: #1d2032;
    --rule: #44465a;
  }
  * { box-sizing: border-box; margin: 0; padding: 0; }
  html, body { width: 1200px; height: 651px; overflow: hidden; }
  body {
    background: var(--stage);
    font-family: "Poppins", sans-serif;
    color: var(--text);
    position: relative;
  }
  .page {
    position: absolute; top: 12px; width: 585px; height: 627px;
    background: var(--footer); overflow: hidden;
  }
  .page--about { left: 12px; }
  .page--readings { left: 603px; }

  .site-nav {
    position: absolute; left: 0; top: 0; width: 100%; height: 41px;
    background: var(--nav); display: flex; align-items: center;
    padding: 0 12px; z-index: 2;
  }
  .brand-dot { width: 28px; height: 28px; border-radius: 50%; background: var(--cream); }
  .nav-links { margin-left: auto; display: flex; gap: 25px; list-style: none; font-size: 9px; }
  .nav-links li { color: var(--text); }
  .nav-links .is-current { color: var(--green); font-weight: 500; }

  .sky {
    position: absolute; left: 0; top: 41px; width: 100%; height: 415px; overflow: hidden;
    background:
      radial-gradient(ellipse 38% 70% at 62% 35%, rgba(90,78,92,0.55), transparent 70%),
      radial-gradient(ellipse 60% 50% at 40% 80%, rgba(60,66,96,0.5), transparent 75%),
      linear-gradient(180deg, var(--night-mid), var(--night));
  }

  .glass {
    position: absolute; background: var(--card);
    border: 1px solid var(--card-line); border-radius: 10px;
  }
  .display { font-family: "Gideon Roman", serif; color: var(--cream); font-weight: 400; }

  /* About hero */
  .hero { left: 44px; top: 21px; width: 489px; height: 377px; text-align: center; }
  .hero-title { position: absolute; left: 0; width: 100%; top: 34px; font-size: 27px; line-height: 29px; }
  .hero-copy {
    position: absolute; left: 40px; width: 409px; top: 112px;
    font-size: 11.2px; line-height: 14.7px; font-weight: 300; color: var(--text);
  }
  .hero-illustration {
    position: absolute; left: 228px; top: 260px; width: 54px; height: 117px;
    border-radius: 4px 4px 0 0;
    background: linear-gradient(180deg, #4b4f73 0%, #3a3d5c 45%, #8fd94f 50%, #2c2f48 70%);
  }

  /* Readings */
  .intro { left: 44px; top: 21px; width: 489px; height: 116px; text-align: center; }
  .intro-title { position: absolute; left: 0; width: 100%; top: 21px; font-size: 24px; line-height: 30px; }
  .intro-copy { position: absolute; left: 30px; width: 429px; top: 64px; font-size: 10.5px; line-height: 14.6px; font-weight: 300; }

  .reading { width: 238px; height: 103px; }
  .reading--birth { left: 44px; top: 169px; border-color: var(--green); box-shadow: 0 0 9px rgba(166,255,92,0.45); }
  .reading--love { left: 295px; top: 169px; }
  .reading--career { left: 44px; top: 284px; }
  .reading--year { left: 295px; top: 284px; }
  .reading-icon {
    position: absolute; left: 16px; top: 28px; width: 48px; height: 48px;
    border-radius: 8px; background: linear-gradient(135deg, rgba(253,243,225,0.28), rgba(253,243,225,0.08));
  }
  .reading--birth .reading-icon { background: linear-gradient(135deg, rgba(166,255,92,0.35), rgba(166,255,92,0.1)); }
  .reading-body { position: absolute; left: 80px; width: 150px; top: 28px; text-align: center; }
  .reading-title { font-size: 14px; line-height: 18px; }
  .reading--birth .reading-title { color: var(--green); }
  .reading-desc { font-size: 7.5px; line-height: 8px; color: var(--text); margin-top: 4px; }
  .reading-link {
    position: absolute; right: 11px; bottom: 7px; display: flex; align-items: center; gap: 6px;
    font-size: 6.7px; color: var(--green);
  }

  /* Footer */
  .site-footer { position: absolute; left: 0; top: 456px; width: 100%; height: 171px; }
  .footer-brand { position: absolute; left: 19px; top: 17px; display: flex; align-items: center; gap: 7px; }
  .footer-brand .dot { width: 20px; height: 20px; border-radius: 50%; background: var(--cream); }
  .footer-brand span { font-family: "Gideon Roman", serif; font-size: 7.5px; line-height: 8px; color: var(--cream); width: 60px; }
  .footer-note { position: absolute; left: 19px; top: 49px; width: 262px; font-size: 6.6px; line-height: 8.4px; color: var(--text); }

  .contact-form { position: absolute; left: 0; top: 0; width: 100%; height: 100%; }
  .field { position: absolute; }
  .field label { display: block; font-size: 6.8px; font-weight: 600; color: var(--text); height: 8px; line-height: 8px; }
  .field .input {
    margin-top: 3px; height: 22px; border-radius: 5px; background: var(--field);
    font-size: 6.8px; color: var(--field-text); line-height: 22px; padding-left: 8px;
  }
  .field--name { left: 289px; top: 28px; width: 134px; }
  .field--birth { left: 433px; top: 28px; width: 135px; }
  .field--country { left: 288px; top: 66px; width: 94px; }
  .field--email { left: 392px; top: 66px; width: 176px; }
  .submit {
    position: absolute; left: 492px; top: 107px; width: 76px; height: 22px;
    border-radius: 5px; background: var(--green); color: var(--ink);
    font-size: 6.8px; font-weight: 600; display: flex; align-items: center; justify-content: center; gap: 5px;
  }
  .footer-rule { position: absolute; left: 17px; right: 17px; top: 140px; height: 1px; background: var(--rule); }
  .copyright { position: absolute; left: 0; width: 100%; top: 152px; text-align: center; font-size: 6.8px; color: var(--muted); }
</style>
</head>
<body>

<section class="page page--about">
  <nav class="site-nav">
    <div class="brand-dot" aria-label="Velvet Harbor Astrology"></div>
    <ul class="nav-links">
      <li class="is-current">About</li><li>Readings</li><li>Booking</li><li>Contact</li><li>Blog</li>
    </ul>
  </nav>
  <div class="sky" role="img" aria-label="Starry night sky with the Milky Way">
    <div class="glass hero">
      <h1 class="display hero-title">Welcome to<br>Velvet Harbor Astrology</h1>
      <p class="hero-copy">Discover the mysteries of the cosmos and gain insight into your journey with our astrology services. Founded on a love for the stars and a passion for guiding others, Velvet Harbor Astrology is dedicated to providing transformative, personalized readings. Our mission is to help you unlock the wisdom of the universe and connect you to your path with clarity and purpose.</p>
      <div class="hero-illustration" role="img" aria-label="Illustration of a person gazing at the moon through a window"></div>
    </div>
  </div>
  <footer class="site-footer">
    <div class="footer-brand"><div class="dot"></div><span>Velvet Harbor Astrology</span></div>
    <p class="footer-note">Have questions or need assistance with booking? We’d love to hear from you! Fill out the form below, or reach out directly via email or phone.</p>
    <div class="contact-form">
      <div class="field field--name"><label>Name</label><div class="input">Name</div></div>
      <div class="field field--birth"><label>Birthdate</label><div class="input">MM - DD - YYYY</div></div>
      <div class="field field--country"><label>Country</label><div class="input">Country</div></div>
      <div class="field field--email"><label>Email Address</label><div class="input">Email</div></div>
      <div class="submit">Get in Touch
        <svg width="6" height="5" viewBox="0 0 6 5"><rect x="0" y="0" width="6" height="5" rx="0.6" fill="#1d2032"/><path d="M0.4 0.6 3 2.7 5.6 0.6" stroke="#a6ff5c" stroke-width="0.6" fill="none"/></svg>
      </div>
    </div>
    <div class="footer-rule"></div>
    <p class="copyright">© Velvet Harbor Astrology. All rights reserved.</p>
  </footer>
</section>

<section class="page page--readings">
  <nav class="site-nav">
    <div class="brand-dot" aria-label="Velvet Harbor Astrology"></div>
    <ul class="nav-links">
      <li>About</li><li class="is-current">Readings</li><li>Booking</li><li>Contact</li><li>Blog</li>
    </ul>
  </nav>
  <div class="sky" role="img" aria-label="Starry night sky with the Milky Way">
    <div class="glass intro">
      <h1 class="display intro-title">Astrology Readings</h1>
      <p class="intro-copy">Choose from our range of readings, each designed to provide insight, clarity, and guidance for different aspects of your life:</p>
    </div>

    <article class="glass reading reading--birth">
      <div class="reading-icon" role="img" aria-label="Line icon of hands cradling a newborn"></div>
      <div class="reading-body">
        <h2 class="display reading-title">Birth Chart Reading</h2>
        <p class="reading-desc">Discover your unique cosmic<br>blueprint.</p>
      </div>
      <div class="reading-link">Let the stars reveal your story
        <svg width="9" height="9" viewBox="0 0 9 9"><path d="M1 8 8 1M3 1h5v5" stroke="#a6ff5c" stroke-width="1" fill="none"/></svg>
      </div>
    </article>

    <article class="glass reading reading--love">
      <div class="reading-icon" role="img" aria-label="Line icon of two hearts with sparkles"></div>
      <div class="reading-body">
        <h2 class="display reading-title">Love Compatibility</h2>
        <p class="reading-desc">Explore the dynamics between<br>you and a partner.</p>
      </div>
    </article>

    <article class="glass reading reading--career">
      <div class="reading-icon" role="img" aria-label="Line icon of a hand holding a briefcase"></div>
      <div class="reading-body">
        <h2 class="display reading-title">Career Path Reading</h2>
        <p class="reading-desc">Uncover the potential paths that<br>align with your energy.</p>
      </div>
    </article>

    <article class="glass reading reading--year">
      <div class="reading-icon" role="img" aria-label="Line icon of a crystal ball with an eye"></div>
      <div class="reading-body">
        <h2 class="display reading-title">Year Ahead Forecast</h2>
        <p class="reading-desc">Gain a sneak peek into the<br>themes of your coming year.</p>
      </div>
    </article>
  </div>
  <footer class="site-footer">
    <div class="footer-brand"><div class="dot"></div><span>Velvet Harbor Astrology</span></div>
    <p class="footer-note">Have questions or need assistance with booking? We’d love to hear from you! Fill out the form below, or reach out directly via email or phone.</p>
    <div class="contact-form">
      <div class="field field--name"><label>Name</label><div class="input">Name</div></div>
      <div class="field field--birth"><label>Birthdate</label><div class="input">MM - DD - YYYY</div></div>
      <div class="field field--country"><label>Country</label><div class="input">Country</div></div>
      <div class="field field--email"><label>Email Address</label><div class="input">Email</div></div>
      <div class="submit">Get in Touch
        <svg width="6" height="5" viewBox="0 0 6 5"><rect x="0" y="0" width="6" height="5" rx="0.6" fill="#1d2032"/><path d="M0.4 0.6 3 2.7 5.6 0.6" stroke="#a6ff5c" stroke-width="0.6" fill="none"/></svg>
      </div>
    </div>
    <div class="footer-rule"></div>
    <p class="copyright">© Velvet Harbor Astrology. All rights reserved.</p>
  </footer>
</section>

</body>
</html>
```